Managed IT services business card design

We haven't needed a business card since the founding of the business in 2005. All our clients have been coming through word of mouth. And lately more and more existing clients are requesting for our business cards to pass on to their contacts in recommending us.
So we needing a business card design. We use various innovative solutions and methodologies to provide IT services to small businesses in managing their IT systems. Our role is the same as an in-house, full-time IT Manager for our clients, but outsourced. So we take care of all our clients' IT needs, just as an IT Manager would be expected to perform.
We have a holding website, which we're happy to leave for now. If we can use the same logo would be great - www.tegvu.com.au
Preferred colours are shades of are white, grey and black.
We pride our business with the following traits: proactive, good service, prompt response, trustworthy.
Target Market(s)
Small businesses of any industry
Industry/Entity Type
Business

```html
<!DOCTYPE html>
<html lang="en">
<head>
<meta charset="utf-8">
<title>Tegvu – Business Card</title>
<link href="https://fonts.googleapis.com/css2?family=Jura:wght@400;500;600&display=swap" rel="stylesheet">
<style>
  :root {
    --card: #ffffff;
    --ink: #2b2b2b;
    --ink-soft: #4a4a4a;
    --rule: #9a9a9a;
    --frame: #a8a8a8;
  }
  * { margin: 0; padding: 0; box-sizing: border-box; }
  html, body {
    width: 1200px;
    height: 1057px;
    overflow: hidden;
    background: var(--card);
  }
  .card {
    position: relative;
    width: 1200px;
    height: 1057px;
    background: var(--card);
    font-family: 'Jura', sans-serif;
    color: var(--ink);
  }
  .brand {
    position: absolute;
    top: 150px;
    left: 0;
    width: 100%;
    display: flex;
    justify-content: center;
    align-items: center;
    gap: 24px;
  }
  .brand-name {
    font-size: 72px;
    font-weight: 500;
    letter-spacing: 1px;
    line-height: 1;
    color: var(--ink);
  }
  .brand-mark {
    width: 22px;
    height: 22px;
    background: var(--ink);
  }
  .frame {
    position: absolute;
    left: 90px;
    top: 400px;
  }
  .holder {
    position: absolute;
    top: 352px;
    right: 150px;
    background: var(--card);
    padding: 0 26px;
  }
  .holder-name {
    font-size: 62px;
    font-weight: 500;
    letter-spacing: 2px;
    line-height: 1.1;
    color: var(--ink);
  }
  .holder-role {
    font-size: 26px;
    font-weight: 500;
    letter-spacing: 3px;
    color: var(--ink-soft);
    margin-top: 2px;
  }
  .contacts {
    position: absolute;
    left: 140px;
    top: 545px;
    width: 860px;
    list-style: none;
  }
  .contact {
    display: flex;
    align-items: center;
    height: 108px;
  }
  .contact-icon {
    flex: 0 0 48px;
    height: 48px;
    border: 2px solid var(--ink-soft);
    display: flex;
    align-items: center;
    justify-content: center;
    font-size: 24px;
    font-weight: 600;
    color: var(--ink);
    margin-right: 46px;
  }
  .contact-text {
    flex: 1;
    font-size: 38px;
    font-weight: 500;
    letter-spacing: 1px;
    color: var(--ink);
    border-bottom: 2px solid var(--rule);
    padding: 10px 0 12px;
    line-height: 1.15;
  }
  .contact:last-child .contact-text { border-bottom: none; }
</style>
</head>
<body>
  <main class="card">
    <div class="brand">
      <span class="brand-name">Tegvu</span>
      <span class="brand-mark" aria-hidden="true"></span>
    </div>

    <svg class="frame" width="1020" height="600" viewBox="0 0 1020 600" aria-hidden="true">
      <rect x="2" y="2" width="1016" height="596" rx="70" ry="70" fill="none" stroke="var(--frame)" stroke-width="3"/>
    </svg>

    <div class="holder">
      <div class="holder-name">LIAM ARCHER</div>
      <div class="holder-role">GENERAL MANAGER</div>
    </div>

    <ul class="contacts">
      <li class="contact"><span class="contact-icon">P</span><span class="contact-text">013 482 7605</span></li>
      <li class="contact"><span class="contact-icon">E</span><span class="contact-text">liam@tegvumail.com</span></li>
      <li class="contact"><span class="contact-icon">W</span><span class="contact-text">www.tegvumanaged.com</span></li>
      <li class="contact"><span class="contact-icon">A</span><span class="contact-text">42 Kellon Road,<br>2nd Floor Arden St W.</span></li>
    </ul>
  </main>
</body>
</html>
```